Cloud Phone Service Brochure

We need a brochure for a Cloud Phone Service offering that we offer in Canada. We're a small company that cares about our client's success and protects their privacy. We would like to see designs that reflect us as a stable, trustworthy company which is also fast moving and leading edge. We see ourselves more like Zelmo than Hask. Sketch Harbor has built our logo and business card, and we look forward to moving ahead here. I've attached our Business Card file so you have our logo as well as my own shot at some thoughts about content written as a trifold. That specific content does not need to be used, nor does it need to be a trifold. Those phone pictures are the actual phones we use.

```html
<!DOCTYPE html>
<html lang="en">
<head>
<meta charset="utf-8">
<title>Cloud Phone Service Brochure</title>
<link href="https://fonts.googleapis.com/css2?family=Roboto+Condensed:wght@400;700&family=PT+Sans:wght@400;700&display=swap" rel="stylesheet">
<style>
:root{
  --bg:#a9a1a3;
  --slate:#3f474b;
  --blue:#2f9fd9;
  --ink:#2b2b2b;
  --white:#ffffff;
}
*{box-sizing:border-box;margin:0;padding:0}
html,body{width:1200px;height:1200px;overflow:hidden;background:var(--bg)}
body{position:relative;font-family:"PT Sans",Arial,sans-serif;color:var(--ink)}
.sheet{position:absolute;left:263px;width:674px;height:524px;background:var(--white);box-shadow:0 6px 10px rgba(0,0,0,.35);overflow:hidden}
.sheet--outside{top:46px}
.sheet--inside{top:623px}
.panel{position:absolute;top:0;height:524px}
.p1{left:0;width:223px}
.p2{left:223px;width:223px}
.p3{left:446px;width:228px}
.fill{position:absolute;left:0;width:100%}
.dark{background:var(--slate);color:var(--white)}
.blue{background:var(--blue);color:var(--white)}
.soft{background:linear-gradient(90deg,#fff 60%,#eceeef)}
.photo{position:absolute;left:0;width:100%}
h2{font-family:"Roboto Condensed",Arial,sans-serif;font-weight:700;line-height:1.1}
h2 .accent{color:var(--blue);text-decoration:underline;text-underline-offset:3px;text-decoration-thickness:1.5px}
ul{list-style:none}
.ticks li,.dots li,.arrows li{font-size:9.6px;line-height:15.2px;position:relative;padding-left:14px}
.ticks li::before{content:"";position:absolute;left:2px;top:4px;width:6px;height:3px;border-left:2px solid currentColor;border-bottom:2px solid currentColor;transform:rotate(-45deg)}
.ticks.blue-tick li::before{border-color:var(--blue)}
.dots li::before{content:"";position:absolute;left:3px;top:6px;width:4px;height:4px;border-radius:50%;background:currentColor}
.dots .sub li{padding-left:28px}
.dots .sub li::before{left:17px;width:4px;height:4px;background:none;border:1px solid currentColor}
.arrows li{padding-left:14px;line-height:12px;margin-bottom:6px}
.arrows li::before{content:"";position:absolute;left:2px;top:3px;border-left:7px solid #fff;border-top:4px solid transparent;border-bottom:4px solid transparent}
.brand{display:flex;align-items:center;gap:6px;font-family:"PT Sans",Arial,sans-serif;font-size:10px;letter-spacing:.5px;color:var(--slate)}
.brand .mark{width:14px;height:14px;background:var(--blue)}
.pill{position:absolute;height:15px;border-radius:8px;color:var(--white);font-size:9.5px;line-height:15px;text-align:center}
.pill.slate{background:var(--slate)}
.pill.blue{background:var(--blue)}
.badges{position:absolute;left:12px;top:448px;width:200px;display:grid;grid-template-columns:repeat(5,1fr);row-gap:14px;justify-items:center}
.badge{width:24px;height:12px;background:#c9ced1;border-radius:2px}
.badge.round{width:14px;height:14px;border-radius:50%}
.center{text-align:center}
</style>
</head>
<body>

<section class="sheet sheet--outside">
  <div class="panel p1">
    <div class="fill dark" style="top:0;height:413px"></div>
    <div class="photo" role="img" aria-label="Black desk IP phone with colour screen" style="top:14px;left:28px;width:140px;height:160px;background:radial-gradient(ellipse at 50% 45%,#2a2d30 40%,#3f474b 75%)"></div>
    <h2 style="position:absolute;left:13px;top:188px;font-size:15px;color:#fff">Phone Service <span class="accent">Features:</span></h2>
    <ul class="ticks" style="position:absolute;left:20px;top:216px;color:#fff">
      <li>All features and functions included</li>
      <li>Conference line included</li>
      <li>Toll Free Number included</li>
      <li>North American LD included</li>
      <li>Monthly billing with no contract</li>
      <li>No hardware or installation costs</li>
      <li>Any high speed internet service</li>
      <li>Keep your existing phone number</li>
      <li>Voicemail to email</li>
      <li>Find Me &amp; Follow Me</li>
      <li>Call Recording</li>
    </ul>
    <h2 class="center" style="position:absolute;left:0;width:223px;top:422px;font-size:15px;color:var(--ink)">Our <span class="accent">Partner</span></h2>
    <div class="badges">
      <span class="badge"></span><span class="badge round"></span><span class="badge"></span><span class="badge"></span><span class="badge round" style="background:#e33"></span>
      <span class="badge"></span><span class="badge round"></span><span class="badge"></span><span class="badge"></span><span class="badge round"></span>
    </div>
  </div>

  <div class="panel p2 soft">
    <div class="fill blue" style="top:0;height:222px"></div>
    <div style="position:absolute;left:20px;top:12px;color:#fff">
      <h2 style="font-family:'PT Sans',Arial,sans-serif;font-size:10px">We are</h2>
      <ul class="dots" style="margin-top:6px"><li>70% Renewable Energy</li><li>100% Renewable for 2020</li></ul>
      <h2 style="font-family:'PT Sans',Arial,sans-serif;font-size:10px;margin-top:18px">We give our time and skills to help</h2>
      <ul class="dots" style="margin-top:6px"><li>Schools</li><li>Community Associations</li><li>Non-profits</li><li>Renewable Energy Initiatives</li></ul>
    </div>
    <div class="photo" role="img" aria-label="Illustration of wind turbines, solar panels and a hydro dam in green countryside" style="left:10px;width:200px;top:178px;height:90px;border:3px solid #fff;background:linear-gradient(180deg,#7fc7ee 0%,#bfe3f5 35%,#7cc042 60%,#3e8f2e 100%)"></div>
    <div class="brand" style="position:absolute;left:42px;top:300px"><span class="mark"></span>VIVID CURRENT</div>
    <svg style="position:absolute;left:104px;top:345px" width="14" height="18" viewBox="0 0 14 18"><path d="M7 0C3 0 0 3 0 7c0 5 7 11 7 11s7-6 7-11c0-4-3-7-7-7z" fill="var(--blue)"/><circle cx="7" cy="7" r="2.6" fill="#fff"/></svg>
    <p class="center" style="position:absolute;left:0;width:223px;top:368px;font-size:9.5px;line-height:12.5px">PO Box 58120<br>14-3080 Larchmere Road NW<br>Calgary, Alberta T2X 4K7 Canada</p>
    <svg style="position:absolute;left:101px;top:425px" width="20" height="14" viewBox="0 0 20 14"><path d="M1 5c0-3 18-3 18 0v2h-5V5H6v2H1z" fill="var(--blue)"/><rect x="3" y="7" width="14" height="7" rx="1" fill="var(--blue)"/><circle cx="10" cy="10.5" r="2" fill="#fff"/></svg>
    <p class="center" style="position:absolute;left:0;width:223px;top:444px;font-size:20px;color:var(--blue)">(403)555-0142</p>
    <div class="pill slate" style="left:38px;width:148px;top:494px">www.vividcurrent.com</div>
  </div>

  <div class="panel p3">
    <div class="brand" style="position:absolute;left:34px;top:30px;font-size:11px"><span class="mark" style="width:16px;height:16px"></span>VIVID CURRENT</div>
    <div class="photo" role="img" aria-label="Office desk phone beneath a cloud PBX diagram linking applications, voicemail, fax and user portal" style="top:60px;height:330px;background:radial-gradient(ellipse at 55% 40%,#7a8fae 0%,#33465e 40%,#101820 85%)"></div>
    <h2 class="center" style="position:absolute;left:0;width:228px;top:404px;font-size:33px;font-weight:400;color:var(--blue)">CLOUD PHONE</h2>
    <h2 class="center" style="position:absolute;left:0;width:228px;top:436px;font-size:56px;color:var(--slate)">SERVICE</h2>
    <div class="pill blue" style="left:41px;width:148px;top:494px">www.vividcurrent.com</div>
  </div>
</section>

<section class="sheet sheet--inside">
  <div class="panel p1 soft">
    <div class="photo" role="img" aria-label="Smiling support agent wearing a headset with a colleague behind" style="top:0;height:207px;background:linear-gradient(90deg,#9aa6b0,#c9ced3 50%,#5b6470)"></div>
    <h2 style="position:absolute;left:14px;top:218px;font-size:15px;color:var(--blue)"><span class="accent" style="color:var(--blue)">Our</span> Services</h2>
    <ul class="ticks blue-tick" style="position:absolute;left:22px;top:249px">
      <li>Network Support</li><li>Phone Service</li><li>Disaster Recovery</li><li>Remote Backups</li><li>Email Archiving</li>
      <li>Desk Suite &amp; Cloudwork Apps</li><li>Migration Services</li><li>Spam and Virus Filtering</li><li>Server and Network Monitoring</li>
      <li>Printing, Scanning and Plotting</li><li>Firewalls and Security</li><li>Network Design and Planning</li>
      <li>Network and Electrical Cabling</li><li>Wireless coverage planning</li><li>Security cameras &amp; Access Control</li>
    </ul>
    <div class="pill blue" style="left:38px;width:148px;top:493px">www.vividcurrent.com</div>
  </div>

  <div class="panel p2 soft">
    <div class="photo" role="img" aria-label="Rows of desk IP phones with colour displays" style="top:0;height:207px;background:linear-gradient(135deg,#e8eaec,#8f99a4 55%,#2d3a46)"></div>
    <h2 style="position:absolute;left:18px;top:218px;font-size:15px;color:var(--blue);font-weight:700">Video Conferencing Room<br><span class="accent" style="color:var(--slate)">Configuration</span></h2>
    <ul class="dots" style="position:absolute;left:24px;top:264px">
      <li>120 Simultaneous video streams</li>
      <li>Most conference sources supported
        <ul class="sub" style="margin:3px 0 3px -14px"><li>Video Conf Room System</li><li>Video Phones</li><li>PC &amp; Lumen Computers</li><li>Robota &amp; Orbit OS Devices</li><li>SIP PBXes</li></ul>
      </li>
      <li style="line-height:12px;margin-bottom:3px">Connect Streamly &amp; Gatherly Live<br>1080p HD at 30 fps</li>
      <li>Multi-location conferencing</li><li>Meeting Controls</li><li>Screen Sharing</li>
      <li>Customizable Registration options</li><li>Email Follow-up options</li><li>10 simultaneous sessions</li><li>Encrypted connections</li>
    </ul>
  </div>

  <div class="panel p3">
    <div class="fill dark" style="top:0;height:228px"></div>
    <h2 style="position:absolute;left:12px;top:9px;font-size:25px;color:var(--blue)">Common Questions</h2>
    <div style="position:absolute;left:14px;top:40px;color:#fff;width:210px">
      <p style="font-size:11px">Why Cloud Service?</p>
      <ul class="arrows" style="margin:5px 0 0 6px">
        <li>Cloud Phones mean no setup costs and no hardware to purchase or support.</li>
        <li>Cloud service also offers seamless remote working and multi-office collaboration.</li>
      </ul>
      <p style="font-size:11px;margin-top:10px;padding-left:3px">Why Vivid Current?</p>
      <ul class="arrows" style="margin:5px 0 0 6px">
        <li>Vivid Current believes in building long term collaborative relationships</li>
        <li>We care about your business as if it was our own.</li>
        <li>Your privacy matters to us. We do not sell, rent or share your data.</li>
      </ul>
    </div>
    <div class="photo" role="img" aria-label="Hand dialing on an office desk phone keypad" style="top:228px;height:90px;background:linear-gradient(90deg,#40505e,#9aa7b3 55%,#e4e7ea)"></div>
    <div class="fill dark" style="top:318px;height:206px"></div>
    <h2 style="position:absolute;left:10px;top:324px;font-size:15px;color:var(--blue)"><span class="accent" style="color:var(--blue)">IP Video Telephony</span></h2>
    <ul class="ticks" style="position:absolute;left:20px;top:349px;color:#fff">
      <li>HD Speakerphone</li><li>HD Video</li><li>7" Touch screen</li><li>Supports Linkwave Headsets</li>
      <li>Built in camera &amp; privacy shutter</li><li>7-way video conferences ondevice</li>
      <li style="line-height:12px;margin-bottom:3px">Fully interoperable with our other phone<br>services</li>
      <li>Ideal for remote workers</li><li>Any high-speed internet service</li><li>Video Conference Room solutions available</li>
    </ul>
  </div>
</section>

</body>
</html>
```